Harlow Estate Solutions Vehicle Wrap 2021 K270

I need a wrap designed for my truck and enclosed trailer. I have a 2021 Brisk K270 GLS 4 door with stock white paint. My enclosed trailer is a 12' V Nose Pellham Hauler. Please note the trailer has split doors in the back and a side door on the right side of the trailer towards the front. I've uploaded a photo of the actual truck and trailer for reference.

Colors: I'd like to incorporate Black, White and Gold into the design for the color palette just like the truck wrap I had designed for a previous vehicle.

Logo: For the logo, I'd like to go with something similar to what is on the example truck wrap in regards to format, however I'd like to consider getting away from the gold outlined house logo portion on the truck, and maybe go with something more like the graphic that is shown on the last uploaded image that has the outline of a roof above HARLOW. I do not like the font in that example however, so I would like to try and go with the font Girard Sky to see how that looks. I'm open to font suggestions, I just don't want generic, and I don't want to see the same wrap I've already uploaded just on a different truck. Same style and flow of design, just refined and cleaned up, keeping things in mind like where the door handles are in relation to the logo and letters, things like.
Please include our website: HESRoofline.example
And our phone: 555-208-4617
Please include the ZUM, TOR and QB TrueClad logos in a similar fashion to the sample truck wrap that I've uploaded for an example.

Target Market(s)

Homeowners

Industry/Entity Type

Roofing & Home Improvement

Font styles to use
Serif
Decorative
Other font styles liked:
• Bullet Small, Girard sky

Requirements
Must have
• clean professional look, website, logo, phone number
Nice to have
• anything subtle that incorporates the state of Indiana and or the city of Indianapolis. Also, anything that would represent or show that we are family owned and locally operated in central Indiana

```html
<!DOCTYPE html>
<html lang="en">
<head>
<meta charset="utf-8">
<title>Harlow Estate Solutions – Identity &amp; Wrap</title>
<link href="https://fonts.googleapis.com/css2?family=Russo+One&family=Exo+2:ital,wght@1,800&family=Orbitron:wght@700&display=swap" rel="stylesheet">
<style>
  :root {
    --page: #eff1f4;
    --ink: #0d0d0d;
    --paper: #ffffff;
    --wrap-black: #1a1816;
    --gold-dark: #a8782e;
    --gold: #d4a94c;
    --gold-light: #f3dc8a;
  }
  * { margin: 0; padding: 0; box-sizing: border-box; }
  html, body { width: 1200px; height: 1001px; overflow: hidden; background: var(--page); }
  .canvas { position: relative; width: 1200px; height: 1001px; }

  .logo-panel {
    position: absolute; top: 159px; width: 504px; height: 234px;
    display: flex; flex-direction: column; align-items: center; justify-content: center;
    padding-top: 18px;
  }
  .logo-panel--light { left: 86px; background: var(--paper); color: var(--ink); }
  .logo-panel--dark { left: 612px; background: var(--ink); color: var(--paper); }
  .logo-name {
    font-family: "Russo One", sans-serif; font-size: 86px; line-height: 1;
    text-transform: lowercase; letter-spacing: 1px;
  }
  .logo-tagline {
    margin-top: 18px; font-family: "Russo One", sans-serif; font-size: 17px;
    letter-spacing: 6px; text-transform: uppercase; color: var(--gold);
  }

  .wrap-layout { position: absolute; left: 90px; top: 570px; width: 1060px; height: 220px; }
  .wrap-layout svg { display: block; }
  .wrap-name { font-family: "Russo One", sans-serif; }
  .wrap-tag { font-family: "Russo One", sans-serif; letter-spacing: 1.6px; }
  .wrap-web { font-family: "Exo 2", sans-serif; font-style: italic; font-weight: 800; }
  .wrap-phone { font-family: "Orbitron", sans-serif; font-weight: 700; letter-spacing: 2px; }
</style>
</head>
<body>
<main class="canvas">
  <section class="logo-panel logo-panel--light">
    <div class="logo-name">harlow</div>
    <div class="logo-tagline">Estate Solutions</div>
  </section>
  <section class="logo-panel logo-panel--dark">
    <div class="logo-name">harlow</div>
    <div class="logo-tagline">Estate Solutions</div>
  </section>

  <section class="wrap-layout" aria-label="Vehicle side wrap layout">
    <svg width="1060" height="220" viewBox="0 0 1060 220">
      <defs>
        <linearGradient id="goldSweep" x1="0" y1="0" x2="1" y2="0">
          <stop offset="0" stop-color="#a8782e"/>
          <stop offset="0.5" stop-color="#f3dc8a"/>
          <stop offset="1" stop-color="#a8782e"/>
        </linearGradient>
      </defs>
      <rect class="wrap-base" x="0" y="0" width="1060" height="220" fill="var(--paper)"/>
      <path class="wrap-band" d="M0 124 L614 124 L658 70 L726 28 L1060 28 L1060 205 L0 205 Z" fill="var(--wrap-black)"/>
      <path class="wrap-stripe" d="M0 118 L618 118 L614 124 L0 124 Z" fill="url(#goldSweep)"/>
      <path class="wrap-stripe" d="M640 120 L720 86 L1010 86 L1010 92 L723 92 L650 122 Z" fill="url(#goldSweep)"/>
      <path class="wrap-stripe" d="M700 113 L1060 113 L1060 119 L696 119 Z" fill="url(#goldSweep)"/>
      <path class="wrap-stripe" d="M0 186 L1060 186 L1060 194 L0 194 Z" fill="url(#goldSweep)"/>

      <text class="wrap-name" x="310" y="102" font-size="34" fill="var(--ink)">harlow</text>
      <text class="wrap-tag" x="311" y="114" font-size="7" fill="var(--gold-dark)">ESTATE SOLUTIONS</text>

      <text class="wrap-web" x="284" y="162" font-size="28" fill="var(--paper)">HES<tspan fill="var(--gold)">ROOFLINE</tspan>.example</text>

      <g class="wrap-phone-icon" transform="translate(750 55)">
        <circle cx="8" cy="8" r="8" fill="none" stroke="var(--paper)" stroke-width="1.5"/>
        <path d="M5 4 L7 4 L8 7 L7 8 Q8 10 9 9 L12 10 L12 12 Q7 13 4 6 Z" fill="var(--paper)"/>
      </g>
      <text class="wrap-phone" x="775" y="71" font-size="19" fill="var(--gold)">555-208-4617</text>
    </svg>
  </section>
</main>
</body>
</html>
```